MES Modul-Struktur grafisch veranschaulichen
Zielgruppe
Wir sind Software-Hersteller. Thema 'MES'. Unsere Kunden sind Produktionsunternehmen.
Mit einem MES (Manufacturing Execution System) werden Produktionsprozesse überwacht, geplant, gesteuert und optimiert. Allgemein geht es darum, die Produktivität zu steigern und Kosten zu minimieren.
Eine MES-Software ist modular strukturiert, so dass der Kunde sich nach Bedarf die einzelnen Funktionsmodule zusammenstellen kann. Unser MES MORVIK 7 MAX besteht z.B. aus folgenden Einzelmodulen:
- BASIS (Basismodul)
- MDE (Maschinendatenerfassung)
- BDE (Betriebsdatenerfassung)
- INST (Instandhaltung)
- ALARM (Alarmierung)
- DOK (Dokumentenmanagement)
- TNT (Traceability)
- PLAN (Feinplanung/Leitstand)
- LOG (Logistik)
- VIS (Visualisierung)
- PEP (Personaleinsatzplanung)
- MPZE (Personalzeiterfassung)
- DNC (Rezepturen/DNC)
- EM (Energiemonitoring)
Aufgabenstellung
Die modulare Struktur und der große Umfang an Modulen ist ein wichtiger Vorteil für unsere Kunden, da Sie nicht so schnell an Grenzen stoßen und sich dann unter Umständen eine weitere Insellösung (extra Software mit extra Datenbank ...) anschaffen müssen.
Wichtig ist, dass die einzelnen Module funktionell ineinandergreifen und alle auf die gleiche Datenbank zugreifen.
Es reicht wenn in der Grafik die Module nur mit er Abkürzung, also z.B. MDE bezeichnet werden. Für den ersten Entwurf können auch Platzhalter genutzt werden.
Der Betrachter sollte aus der Grafik auf den ersten Blick erkennen:
- umfängliches MES
- modular strukturiert
- Funktionsmodule step-by-step erweiterbar
Für die Umsetzung naheliegend wären Puzzle-Steine, Stapolos, ... muss aber nicht.

```html
<!DOCTYPE html>
<html lang="de">
<head>
<meta charset="utf-8">
<title>MES Modulstruktur – MORVIK 7 MAX</title>
<link rel="stylesheet" href="https://fonts.googleapis.com/css2?family=Source+Sans+3:wght@400;700&display=swap">
<style>
  :root{
    --bg-center:#ffffff;
    --bg-edge:#d6dde1;
    --frame:#123f2a;
    --connector:#cfd8dd;
    --hex-frame:#ffffff;
    --ink:#ffffff;
  }
  html,body{margin:0;padding:0;width:1200px;height:1050px;overflow:hidden;}
  body{font-family:"Source Sans 3",sans-serif;}
  .module-map{display:block;width:1200px;height:1050px;}
  .map-frame{fill:url(#bg-glow);stroke:var(--frame);stroke-width:2;}
  .connector{stroke:var(--connector);stroke-width:16;}
  .hex-frame{fill:var(--hex-frame);filter:url(#hex-shadow);}
  .hex-head{fill:var(--head);}
  .hex-body{fill:var(--body);}
  .module-code{font-family:"Source Sans 3",sans-serif;font-weight:700;font-size:35px;fill:var(--ink);text-anchor:middle;}
  .module-name{font-family:"Source Sans 3",sans-serif;font-weight:400;font-size:16px;fill:var(--ink);text-anchor:middle;}
  .icon{fill:none;stroke:var(--ink);stroke-width:5;stroke-linecap:round;stroke-linejoin:round;}
  .icon-fill{fill:var(--ink);stroke:none;}
  .icon-cut{fill:var(--body);stroke:none;}

  .module--basis{--head:#c1d0d8;--body:#ccd8df;}
  .module--bde{--head:#f7b000;--body:#fbc340;}
  .module--alarm{--head:#e54b17;--body:#ec753a;}
  .module--mde{--head:#b7c91f;--body:#c8d75b;}
  .module--inst{--head:#ee8200;--body:#f29c3f;}
  .module--plan{--head:#0c4227;--body:#245c3c;}
  .module--tnt{--head:#5fad27;--body:#89bd54;}
  .module--dok{--head:#046b33;--body:#2b8150;}
  .module--pep{--head:#7bc4ea;--body:#9fd3ef;}
  .module--mpze{--head:#059a3a;--body:#4ba955;}
  .module--log{--head:#302a62;--body:#5d4a7f;}
  .module--vis{--head:#2c93d1;--body:#6ba8d6;}
  .module--dnc{--head:#722f76;--body:#8c5389;}
  .module--em{--head:#0f58a0;--body:#4774b1;}
</style>
</head>
<body>
<svg class="module-map" viewBox="0 0 1417 1240" width="1200" height="1050" role="img" aria-label="MES MORVIK 7 MAX – Modulstruktur als Wabengrafik">
  <defs>
    <radialGradient id="bg-glow" cx="50%" cy="48%" r="70%">
      <stop offset="0" stop-color="var(--bg-center)"/>
      <stop offset="0.55" stop-color="#f1f4f5"/>
      <stop offset="1" stop-color="var(--bg-edge)"/>
    </radialGradient>
    <filter id="hex-shadow" x="-20%" y="-20%" width="140%" height="140%">
      <feDropShadow dx="3" dy="5" stdDeviation="6" flood-color="#5d6a72" flood-opacity="0.35"/>
    </filter>
    <polygon id="hex-outer" points="-148,0 -76,-130 76,-130 148,0 76,130 -76,130"/>
    <polygon id="hex-top" points="-122,1 -62,-107 62,-107 122,1"/>
    <polygon id="hex-bottom" points="-122,0 122,0 62,107 -62,107"/>
  </defs>

  <rect class="map-frame" x="1" y="1" width="1415" height="1238"/>

  <g class="connectors">
    <line class="connector" x1="705" y1="200" x2="705" y2="485"/>
    <line class="connector" x1="705" y1="485" x2="707" y2="768"/>
    <line class="connector" x1="707" y1="768" x2="709" y2="1055"/>
    <line class="connector" x1="462" y1="340" x2="462" y2="630"/>
    <line class="connector" x1="462" y1="630" x2="464" y2="915"/>
    <line class="connector" x1="948" y1="340" x2="950" y2="625"/>
    <line class="connector" x1="950" y1="625" x2="953" y2="912"/>
    <line class="connector" x1="220" y1="485" x2="218" y2="770"/>
    <line class="connector" x1="1195" y1="485" x2="1195" y2="770"/>
    <line class="connector" x1="705" y1="200" x2="462" y2="340"/>
    <line class="connector" x1="705" y1="200" x2="948" y2="340"/>
    <line class="connector" x1="462" y1="340" x2="705" y2="485"/>
    <line class="connector" x1="948" y1="340" x2="705" y2="485"/>
    <line class="connector" x1="462" y1="340" x2="220" y2="485"/>
    <line class="connector" x1="220" y1="485" x2="462" y2="630"/>
    <line class="connector" x1="705" y1="485" x2="462" y2="630"/>
    <line class="connector" x1="705" y1="485" x2="950" y2="625"/>
    <line class="connector" x1="948" y1="340" x2="1195" y2="485"/>
    <line class="connector" x1="1195" y1="485" x2="950" y2="625"/>
    <line class="connector" x1="462" y1="630" x2="218" y2="770"/>
    <line class="connector" x1="218" y1="770" x2="464" y2="915"/>
    <line class="connector" x1="462" y1="630" x2="707" y2="768"/>
    <line class="connector" x1="950" y1="625" x2="707" y2="768"/>
    <line class="connector" x1="950" y1="625" x2="1195" y2="770"/>
    <line class="connector" x1="1195" y1="770" x2="953" y2="912"/>
    <line class="connector" x1="464" y1="915" x2="707" y2="768"/>
    <line class="connector" x1="707" y1="768" x2="953" y2="912"/>
    <line class="connector" x1="464" y1="915" x2="709" y2="1055"/>
    <line class="connector" x1="953" y1="912" x2="709" y2="1055"/>
  </g>

  <!-- BASIS -->
  <g class="module module--basis" transform="translate(705,200)">
    <use href="#hex-outer" class="hex-frame"/>
    <use href="#hex-bottom" class="hex-body"/>
    <use href="#hex-top" class="hex-head"/>
    <text class="module-code" y="-48">BASIS</text>
    <text class="module-name" y="-25">Basismodul</text>
    <g transform="translate(0,48)">
      <path class="icon-fill" d="M0,42 C-14,22 -26,8 -26,-8 A26,26 0 1 1 26,-8 C26,8 14,22 0,42Z"/>
      <circle class="icon-cut" cx="0" cy="-8" r="9"/>
    </g>
  </g>

  <!-- BDE -->
  <g class="module module--bde" transform="translate(462,340)">
    <use href="#hex-outer" class="hex-frame"/>
    <use href="#hex-bottom" class="hex-body"/>
    <use href="#hex-top" class="hex-head"/>
    <text class="module-code" y="-46">BDE</text>
    <text class="module-name" y="-23">Betriebsdatenerfassung</text>
    <g transform="translate(0,56)">
      <path class="icon" style="stroke-width:3" d="M-34,-28 V28 H34"/>
      <rect class="icon-fill" x="-28" y="-10" width="6" height="34"/>
      <rect class="icon-fill" x="-18" y="-22" width="6" height="46"/>
      <rect class="icon-fill" x="-8" y="2" width="6" height="22"/>
      <rect class="icon-fill" x="2" y="8" width="6" height="16"/>
      <circle class="icon" style="stroke-width:4" cx="6" cy="-10" r="13"/>
      <path class="icon" style="stroke-width:6" d="M16,0 L30,16"/>
    </g>
  </g>

  <!-- ALARM -->
  <g class="module module--alarm" transform="translate(948,340)">
    <use href="#hex-outer" class="hex-frame"/>
    <use href="#hex-bottom" class="hex-body"/>
    <use href="#hex-top" class="hex-head"/>
    <text class="module-code" y="-46">ALARM</text>
    <text class="module-name" y="-23">Alarmierung</text>
    <g transform="translate(0,54)">
      <circle class="icon-fill" r="10"/>
      <path class="icon" d="M-20,-18 A26,26 0 0 0 -20,18 M20,-18 A26,26 0 0 1 20,18"/>
      <path class="icon" d="M-32,-28 A42,42 0 0 0 -32,28 M32,-28 A42,42 0 0 1 32,28"/>
    </g>
  </g>

  <!-- MDE -->
  <g class="module module--mde" transform="translate(220,485)">
    <use href="#hex-outer" class="hex-frame"/>
    <use href="#hex-bottom" class="hex-body"/>
    <use href="#hex-top" class="hex-head"/>
    <text class="module-code" y="-43">MDE</text>
    <text class="module-name" y="-20">Maschinendatenerfassung</text>
    <g transform="translate(0,52)">
      <circle class="icon" style="stroke-width:6;stroke-dasharray:4 3.5" cx="-20" cy="10" r="14"/>
      <circle class="icon" style="stroke-width:3" cx="-20" cy="10" r="8"/>
      <circle class="icon" style="stroke-width:5;stroke-dasharray:3.5 3" cx="4" cy="-14" r="10"/>
      <circle class="icon" style="stroke-width:3" cx="4" cy="-14" r="5"/>
      <path class="icon" style="stroke-width:4" d="M0,24 L34,-10 L42,-2 L8,32 L-2,34 Z"/>
    </g>
  </g>

  <!-- INST -->
  <g class="module module--inst" transform="translate(705,485)">
    <use href="#hex-outer" class="hex-frame"/>
    <use href="#hex-bottom" class="hex-body"/>
    <use href="#hex-top" class="hex-head"/>
    <text class="module-code" y="-48">INST</text>
    <text class="module-name" y="-25">Instandhaltung</text>
    <g transform="translate(0,52)">
      <path class="icon" style="stroke-width:8" d="M-22,-22 L24,24"/>
      <path class="icon" style="stroke-width:6" d="M-28,-28 L-20,-30 L-30,-20 Z"/>
      <path class="icon" style="stroke-width:8" d="M22,-22 L-22,22"/>
      <circle class="icon" style="stroke-width:6" cx="24" cy="-24" r="7"/>
      <circle class="icon-fill" cx="-26" cy="26" r="6"/>
    </g>
  </g>

  <!-- PLAN -->
  <g class="module module--plan" transform="translate(1195,485)">
    <use href="#hex-outer" class="hex-frame"/>
    <use href="#hex-bottom" class="hex-body"/>
    <use href="#hex-top" class="hex-head"/>
    <text class="module-code" y="-48">PLAN</text>
    <text class="module-name" y="-25">Feinplanung/Leitstand</text>
    <g transform="translate(0,56)">
      <rect class="icon" style="stroke-width:4" x="-30" y="-26" width="60" height="54" rx="5"/>
      <path class="icon" style="stroke-width:4" d="M-30,-12 H30 M-16,-34 V-20 M16,-34 V-20"/>
      <rect class="icon-fill" x="-22" y="-4" width="12" height="10"/>
      <rect class="icon-fill" x="-6" y="-4" width="12" height="10"/>
      <rect class="icon-fill" x="10" y="-4" width="12" height="10"/>
      <rect class="icon-fill" x="-22" y="10" width="12" height="10"/>
      <rect class="icon-fill" x="-6" y="10" width="12" height="10"/>
      <rect class="icon-fill" x="10" y="10" width="12" height="10"/>
    </g>
  </g>

  <!-- TNT -->
  <g class="module module--tnt" transform="translate(462,630)">
    <use href="#hex-outer" class="hex-frame"/>
    <use href="#hex-bottom" class="hex-body"/>
    <use href="#hex-top" class="hex-head"/>
    <text class="module-code" y="-44">TNT</text>
    <text class="module-name" y="-21">Traceability</text>
    <g transform="translate(0,54)">
      <path class="icon" style="stroke-width:7;stroke-linecap:butt" d="M-32,-14 H-16 C-4,-14 4,14 16,14 H24"/>
      <path class="icon" style="stroke-width:7;stroke-linecap:butt" d="M-32,14 H-16 C-4,14 4,-14 16,-14 H24"/>
      <path class="icon-fill" d="M22,-26 L36,-14 L22,-2 Z M22,2 L36,14 L22,26 Z"/>
    </g>
  </g>

  <!-- DOK -->
  <g class="module module--dok" transform="translate(950,625)">
    <use href="#hex-outer" class="hex-frame"/>
    <use href="#hex-bottom" class="hex-body"/>
    <use href="#hex-top" class="hex-head"/>
    <text class="module-code" y="-46">DOK</text>
    <text class="module-name" y="-23">Dokumentenmanagement</text>
    <g transform="translate(0,56)">
      <path class="icon" style="stroke-width:4" d="M-20,-30 H8 L22,-16 V30 H-20 Z M8,-30 V-16 H22"/>
      <path class="icon" style="stroke-width:4;stroke-linecap:butt" d="M-12,-4 H14 M-12,6 H14 M-12,16 H14"/>
    </g>
  </g>

  <!-- PEP -->
  <g class="module module--pep" transform="translate(218,770)">
    <use href="#hex-outer" class="hex-frame"/>
    <use href="#hex-bottom" class="hex-body"/>
    <use href="#hex-top" class="hex-head"/>
    <text class="module-code" y="-43">PEP</text>
    <text class="module-name" y="-20">Personaleinsatzplanung</text>
    <g transform="translate(0,54)" class="icon-fill">
      <circle cx="-22" cy="-24" r="7"/>
      <rect x="-32" y="-14" width="20" height="24" rx="4"/>
      <rect x="-29" y="8" width="14" height="16"/>
      <circle cx="22" cy="-24" r="7"/>
      <rect x="12" y="-14" width="20" height="24" rx="4"/>
      <rect x="15" y="8" width="14" height="16"/>
      <circle cx="0" cy="-18" r="8" style="stroke:var(--body);stroke-width:2"/>
      <rect x="-12" y="-8" width="24" height="26" rx="4" style="stroke:var(--body);stroke-width:2"/>
      <rect x="-8" y="16" width="16" height="18" style="stroke:var(--body);stroke-width:2"/>
    </g>
  </g>

  <!-- MPZE -->
  <g class="module module--mpze" transform="translate(707,768)">
    <use href="#hex-outer" class="hex-frame"/>
    <use href="#hex-bottom" class="hex-body"/>
    <use href="#hex-top" class="hex-head"/>
    <text class="module-code" y="-44">MPZE</text>
    <text class="module-name" y="-21">Personalzeiterfassung</text>
    <g transform="translate(0,54)">
      <circle class="icon" style="stroke-width:4" r="30"/>
      <path class="icon" style="stroke-width:3" d="M0,-26 V-21 M0,21 V26 M-26,0 H-21 M21,0 H26"/>
      <path class="icon" style="stroke-width:3" d="M-14,-4 L0,2 L18,-6"/>
    </g>
  </g>

  <!-- LOG -->
  <g class="module module--log" transform="translate(1195,770)">
    <use href="#hex-outer" class="hex-frame"/>
    <use href="#hex-bottom" class="hex-body"/>
    <use href="#hex-top" class="hex-head"/>
    <text class="module-code" y="-45">LOG</text>
    <text class="module-name" y="-22">Logistik</text>
    <g transform="translate(0,52)">
      <path class="icon-fill" d="M-36,-24 H12 L28,-6 L40,0 V20 H-36 Z"/>
      <path class="icon-cut" d="M16,-20 H10 V-4 H28 Z"/>
      <rect class="icon-cut" x="-36" y="6" width="76" height="3"/>
      <circle class="icon-fill" cx="-18" cy="22" r="9" style="stroke:var(--body);stroke-width:3"/>
      <circle class="icon-fill" cx="26" cy="22" r="9" style="stroke:var(--body);stroke-width:3"/>
      <circle class="icon-cut" cx="-18" cy="22" r="3"/>
      <circle class="icon-cut" cx="26" cy="22" r="3"/>
    </g>
  </g>

  <!-- VIS -->
  <g class="module module--vis" transform="translate(464,915)">
    <use href="#hex-outer" class="hex-frame"/>
    <use href="#hex-bottom" class="hex-body"/>
    <use href="#hex-top" class="hex-head"/>
    <text class="module-code" y="-43">VIS</text>
    <text class="module-name" y="-20">Visualisierung</text>
    <g transform="translate(0,54)">
      <path class="icon-fill" d="M-44,0 C-26,-26 26,-26 44,0 C26,26 -26,26 -44,0 Z"/>
      <path class="icon-cut" d="M-34,0 C-20,-18 20,-18 34,0 C20,18 -20,18 -34,0 Z"/>
      <circle class="icon-fill" r="14"/>
      <circle class="icon-cut" r="6"/>
    </g>
  </g>

  <!-- DNC -->
  <g class="module module--dnc" transform="translate(953,912)">
    <use href="#hex-outer" class="hex-frame"/>
    <use href="#hex-bottom" class="hex-body"/>
    <use href="#hex-top" class="hex-head"/>
    <text class="module-code" y="-42">DNC</text>
    <text class="module-name" y="-20">Rezepturen/DNC</text>
    <g transform="translate(0,56)">
      <path class="icon" style="stroke-width:3" d="M0,-18 V4 M-22,4 H22 M-22,4 V14 M0,4 V14 M22,4 V14"/>
      <rect class="icon-fill" x="-8" y="-28" width="16" height="14"/>
      <rect class="icon-fill" x="-30" y="12" width="16" height="14"/>
      <rect class="icon-fill" x="-8" y="12" width="16" height="14"/>
      <rect class="icon-fill" x="14" y="12" width="16" height="14"/>
    </g>
  </g>

  <!-- EM -->
  <g class="module module--em" transform="translate(709,1055)">
    <use href="#hex-outer" class="hex-frame"/>
    <use href="#hex-bottom" class="hex-body"/>
    <use href="#hex-top" class="hex-head"/>
    <text class="module-code" y="-42">EM</text>
    <text class="module-name" y="-20">Energiemonitoring</text>
    <g transform="translate(0,52)">
      <rect class="icon-fill" x="-34" y="-18" width="66" height="36" rx="3"/>
      <rect class="icon-fill" x="32" y="-8" width="6" height="16"/>
      <path class="icon-cut" d="M-6,-12 H26 V12 H-26 Z"/>
    </g>
  </g>
</svg>
</body>
</html>
```